Yard sign for Chimney Buisness

I am looking for a 18 Tall x 24" wide yard sign design incorporating our logo/name. We want the signs to stand out and be readable from a distance. only want our logo/business name and website on the sign . www.flintmorrowvt.com

Target Market(s)

homeowners

Requirements
Must have
• logo/buisness name
• website
• must be visable at a distance and readable

```html
<!DOCTYPE html>
<html lang="en">
<head>
<meta charset="utf-8">
<title>Flintmorrow Yard Sign Colourways</title>
<link rel="stylesheet" href="https://fonts.googleapis.com/css2?family=Bebas+Neue&family=Cinzel:wght@500&display=swap">
<style>
  :root {
    --page: #ffffff;
    --navy: #0c2033;
    --navy-band: #e1deda;
    --navy-url: #2a0a0a;
    --sage: #4f6457;
    --sage-band: #d7b24a;
    --sage-url: #262626;
    --black: #111111;
    --black-band: #ead600;
    --black-url: #111111;
    --sky: #99d3e1;
    --sky-band: #df6489;
    --sky-url: #f0ece4;
    --cream: #e6e3dc;
    --charcoal: #2b2b2b;
  }
  html, body {
    margin: 0;
    padding: 0;
    width: 1200px;
    height: 965px;
    overflow: hidden;
    background: var(--page);
  }
  .sheet {
    position: relative;
    width: 1200px;
    height: 965px;
  }
  .sign {
    position: absolute;
    width: 538px;
    height: 403px;
    background: var(--bg);
    color: var(--ink);
  }
  .sign--navy  { left: 42px;  top: 57px;  --bg: var(--navy);  --ink: var(--cream);    --band: var(--navy-band);  --url: var(--navy-url); }
  .sign--sage  { left: 619px; top: 63px;  --bg: var(--sage);  --ink: var(--cream);    --band: var(--sage-band);  --url: var(--sage-url); }
  .sign--black { left: 44px;  top: 498px; --bg: var(--black); --ink: var(--cream);    --band: var(--black-band); --url: var(--black-url); }
  .sign--sky   { left: 618px; top: 504px; --bg: var(--sky);   --ink: var(--charcoal); --band: var(--sky-band);   --url: var(--sky-url); }

  .brand-square {
    position: absolute;
    left: 50%;
    top: 50px;
    width: 122px;
    height: 122px;
    margin-left: -73px;
    border: 12px solid var(--ink);
  }
  .brand-name {
    position: absolute;
    left: 0;
    right: 0;
    top: 214px;
    margin: 0;
    text-align: center;
    font-family: "Cinzel", serif;
    font-weight: 500;
    font-size: 42px;
    line-height: 1;
    letter-spacing: 2px;
    color: var(--ink);
  }
  .url-band {
    position: absolute;
    left: 0;
    right: 0;
    top: 314px;
    height: 72px;
    background: var(--band);
    display: flex;
    align-items: center;
    justify-content: center;
  }
  .url {
    font-family: "Bebas Neue", sans-serif;
    font-size: 52px;
    line-height: 1;
    letter-spacing: 2px;
    color: var(--url);
    padding-top: 5px;
    white-space: nowrap;
  }
</style>
</head>
<body>
<main class="sheet">
  <section class="sign sign--navy">
    <div class="brand-square"></div>
    <h2 class="brand-name">FLINTMORROW</h2>
    <div class="url-band"><span class="url">WWW.FLINTMORROWVT.COM</span></div>
  </section>
  <section class="sign sign--sage">
    <div class="brand-square"></div>
    <h2 class="brand-name">FLINTMORROW</h2>
    <div class="url-band"><span class="url">WWW.FLINTMORROWVT.COM</span></div>
  </section>
  <section class="sign sign--black">
    <div class="brand-square"></div>
    <h2 class="brand-name">FLINTMORROW</h2>
    <div class="url-band"><span class="url">WWW.FLINTMORROWVT.COM</span></div>
  </section>
  <section class="sign sign--sky">
    <div class="brand-square"></div>
    <h2 class="brand-name">FLINTMORROW</h2>
    <div class="url-band"><span class="url">WWW.FLINTMORROWVT.COM</span></div>
  </section>
</main>
</body>
</html>
```